Buffet Restaurant A0 poster for pavement A Board

We are an 'All you can eat' buffet restaurant in a large competitive shopping mall in the UK. We need a size A0 poster for an 'A board' to stand outside our restaurant on the mall to attract customers. The minimum it has to say is that the price is £9.99. Simple!

Please note: the shop front sign on the photos is not blue, it white led backlit that looks blue on photo. Also logo is very simple text you can see on sign. Also check out tallfernos.net

Target Market(s)

Passers by (see Quaybridge demographic via google search)

Industry/Entity Type

Restaurant

Font styles to use
Sans Serif

Requirements
Must have
• Must do the job of enticing customers to our door

```html
<!DOCTYPE html>
<html lang="en">
<head>
<meta charset="utf-8">
<title>Tall Fernos World Buffet – A Board Poster</title>
<link rel="stylesheet" href="https://fonts.googleapis.com/css2?family=Carlito:ital,wght@0,400;0,700;1,400&display=swap">
<style>
  :root {
    --canvas: #ffffff;
    --mustard: #b08100;
    --ink: #0d0b08;
    --banner-dark: #1d1f21;
    --banner-mid: #3a3d40;
    --banner-text: #ffffff;
  }
  * { margin: 0; padding: 0; box-sizing: border-box; }
  html, body {
    width: 1000px; height: 1200px; overflow: hidden;
    background: var(--canvas);
  }
  .poster {
    position: relative; width: 1000px; height: 1200px;
    font-family: "Carlito", "Calibri", sans-serif; color: var(--ink);
  }
  .board {
    position: absolute; left: 82px; top: 12px; width: 833px; height: 1178px;
    background: var(--mustard);
  }
  .line {
    position: absolute; left: 0; width: 1000px; text-align: center; white-space: nowrap;
  }
  .headline { top: 50px; font-size: 42px; font-weight: 700; }
  .question { top: 136px; font-size: 25px; }
  .all-you-can-eat { top: 182px; font-size: 48px; font-style: italic; }
  .all-you-can-eat strong { font-style: normal; font-weight: 700; }
  .only { top: 292px; font-size: 30px; }
  .price { top: 330px; left: 6px; font-weight: 700; line-height: 1; }
  .price .currency { font-size: 92px; font-weight: 400; vertical-align: 22px; margin-right: 6px; }
  .price .amount { font-size: 196px; letter-spacing: 2px; }

  .banner {
    position: absolute; left: 80px; top: 560px; width: 835px; height: 318px;
    color: var(--banner-text); overflow: hidden;
  }
  .banner-photo {
    position: absolute; inset: 0;
    background: linear-gradient(180deg, var(--banner-mid) 0%, var(--banner-dark) 55%, #2b2d2f 100%);
  }
  .brand-name {
    position: absolute; top: 74px; width: 100%; text-align: center;
    font-family: "Carlito", "Calibri", sans-serif; font-weight: 700;
    font-size: 112px; line-height: 1.05; letter-spacing: 1px;
    color: var(--banner-text);
  }
  .brand-name span { display: block; font-size: 48px; }

  .kids-price, .baby-price { position: absolute; top: 898px; font-size: 21px; }
  .kids-price { left: 124px; }
  .baby-price { right: 140px; }
  .spirits { top: 1006px; font-size: 42px; font-weight: 700; }
</style>
</head>
<body>
  <main class="poster">
    <div class="board"></div>

    <h1 class="line headline">Fresh, Fast, Quality Offerings</h1>
    <p class="line question">What else can we say?</p>
    <p class="line all-you-can-eat">Besides <strong>ALL</strong> you can eat?</p>
    <p class="line only">Howay man! Only</p>
    <p class="line price"><span class="currency">£</span><span class="amount">9.99</span></p>

    <section class="banner">
      <div class="banner-photo" role="img" aria-label="Dimmed photograph of the buffet counter and serving dishes"></div>
      <p class="brand-name">TALL FERNOS<span>WORLD BUFFET</span></p>
    </section>

    <p class="kids-price">Children under 12 £4.50</p>
    <p class="baby-price">Babies in high chairs&nbsp; £1.50</p>

    <p class="line spirits">Spirits’ Available</p>
  </main>
</body>
</html>
```